CareRally442 Core Services Brochure
Professional marketing brochure
CareRally442 Core Services Brochure - Emergency Services
Creative Brief
Emergency Services
Customers; Destination Management Companies, Event Planners, Event Coordinators, production companies, federal government (forest service, TVR), security companies/managers, EMT’s Paramedics, Healthcare Professionals
We are looking for a professional & unique trifold brochure (consider other designs) providing an overview of our core services (Event Standby, Wildland, Medical Escort, CPR & First Aid Training) We do not want to follow the traditional “fold” limitations, See BriefExample1. At the end of the contest we want the complete .psd (photoshop), .ind (indesign) or AI file.

```html
<!DOCTYPE html>
<html lang="en">
<head>
<meta charset="utf-8">
<title>CareRally442 Core Services Brochure</title>
<link href="https://fonts.googleapis.com/css2?family=Oswald:wght@400;500;600;700&family=Open+Sans:wght@400;600;700&display=swap" rel="stylesheet">
<style>
  :root{
    --stage:#8e8e8e;
    --paper:#ffffff;
    --brand-blue:#1f5fb0;
    --deep-blue:#0d3f86;
    --sky-blue:#3f8ad6;
    --charcoal:#3b3d41;
    --slate:#5b5e63;
    --orange:#e8731e;
    --text-gray:#5a5a5a;
  }
  *{box-sizing:border-box;margin:0;padding:0}
  html,body{width:1200px;height:901px;overflow:hidden}
  body{background:var(--stage);font-family:"Open Sans",sans-serif;position:relative}

  .panel{position:absolute;top:90px;height:720px;background:var(--paper);overflow:hidden;box-shadow:0 6px 18px rgba(0,0,0,.25)}

  /* front cover */
  .cover{left:40px;width:320px}
  .cover-brand{position:absolute;top:48px;left:0;right:0;display:flex;align-items:center;justify-content:center;gap:10px}
  .brand-name{font-family:"Oswald",sans-serif;font-weight:600;font-size:30px;color:var(--brand-blue);letter-spacing:.5px}
  .brand-dot{width:26px;height:26px;border-radius:50%;background:var(--brand-blue)}
  .cover-swoosh{position:absolute;top:118px;left:0;width:320px;height:70px}
  .cover-photo{position:absolute;top:160px;left:0;right:0;bottom:0;background:linear-gradient(160deg,#6d7075 0%,#2f3236 55%,#1c1e21 100%)}
  .cover-url{position:absolute;bottom:22px;left:22px;font-family:"Oswald",sans-serif;font-size:14px;color:#fff;letter-spacing:.4px}

  /* inside spread */
  .spread-left{left:400px;width:380px}
  .spread-right{left:780px;width:380px;box-shadow:6px 6px 18px rgba(0,0,0,.25)}
  .fold{position:absolute;top:90px;left:779px;width:2px;height:720px;background:rgba(0,0,0,.18)}

  .photo{position:absolute}
  .photo-team{top:0;left:0;width:380px;height:150px;background:linear-gradient(135deg,#7b8a6a,#4b5a44 60%,#2f3a2c)}
  .clients{position:absolute;top:150px;left:0;width:380px;height:340px;background:var(--charcoal);padding:26px 30px}
  .clients-title{font-family:"Oswald",sans-serif;font-weight:700;font-size:34px;color:#fff;letter-spacing:.5px;margin-bottom:14px}
  .clients-list{list-style:none;font-family:"Oswald",sans-serif;font-weight:500;font-size:17px;line-height:1.38;color:#e9e9e9;text-transform:uppercase}
  .photo-stadium{top:490px;left:0;width:190px;height:230px;background:linear-gradient(180deg,#6f9bd0,#4a7f3e 55%,#7a5b3e)}
  .photo-crew{top:490px;left:192px;width:188px;height:114px;background:linear-gradient(180deg,#a7c1e0,#c9b46a)}
  .photo-vehicle{top:606px;left:192px;width:188px;height:114px;background:linear-gradient(160deg,#d7dbe0,#8e959d)}

  .intro{position:absolute;top:0;left:0;width:380px;height:250px;padding:26px 28px}
  .intro-title{font-family:"Oswald",sans-serif;font-weight:600;font-size:16px;color:var(--orange);text-transform:uppercase;line-height:1.25;margin-bottom:12px}
  .intro-text{font-size:11.5px;line-height:1.6;color:var(--text-gray)}
  .specialize{position:absolute;top:250px;left:0;width:380px;height:250px;background:linear-gradient(180deg,var(--sky-blue),var(--deep-blue));padding:28px 28px}
  .specialize-title{font-family:"Oswald",sans-serif;font-weight:700;font-size:36px;color:#fff;margin-bottom:12px}
  .specialize-text{font-size:12px;line-height:1.6;color:#eef4fb}
  .photo-ambulance{top:500px;left:0;width:126px;height:220px;background:linear-gradient(170deg,#e48a2e,#8a4a1c)}
  .photo-medic{top:500px;left:127px;width:126px;height:220px;background:linear-gradient(180deg,#b8c7d6,#c9572a 60%,#5a3a2a)}
  .photo-balloon{top:500px;left:254px;width:126px;height:220px;background:linear-gradient(180deg,#2a2038,#d2522a 60%,#f0a03a)}
</style>
</head>
<body>

  <section class="panel cover">
    <div class="cover-brand">
      <span class="brand-name">CareRally442</span>
      <span class="brand-dot"></span>
    </div>
    <div class="cover-photo" role="img" aria-label="Photo of a metal danger warning sign with a chain"></div>
    <svg class="cover-swoosh" viewBox="0 0 320 70" preserveAspectRatio="none">
      <path d="M0 42 C110 10 220 10 320 30 L320 0 L0 0 Z" fill="#ffffff"/>
      <path d="M0 42 C110 10 220 10 320 30 L320 40 C220 22 110 24 0 54 Z" fill="#1f5fb0"/>
    </svg>
    <p class="cover-url">www.CareRally442.com</p>
  </section>

  <section class="panel spread-left">
    <div class="photo photo-team" role="img" aria-label="Photo of the medical team at a mountain event"></div>
    <div class="clients">
      <h2 class="clients-title">WHO WE WORK WITH!</h2>
      <ul class="clients-list">
        <li>DMC's / Travel Destination Management</li>
        <li>Companies Event Planners</li>
        <li>Event Coordinators</li>
        <li>Production Companies</li>
        <li>Federal Government</li>
        <li>Forest Service TVR Security</li>
        <li>Companies / Managers</li>
        <li>EMT's Paramedics Healthcare</li>
        <li>Professionals</li>
      </ul>
    </div>
    <div class="photo photo-stadium" role="img" aria-label="Photo of a crowded baseball stadium"></div>
    <div class="photo photo-crew" role="img" aria-label="Photo of wildland crew in yellow shirts"></div>
    <div class="photo photo-vehicle" role="img" aria-label="Photo of response vehicles on site"></div>
  </section>

  <section class="panel spread-right">
    <div class="intro">
      <h3 class="intro-title">We exist for your customer's to know that they do</h3>
      <p class="intro-text">Our team gives event hosts calm confidence. Certified medics stand ready on site so guests, crews and staff stay safe while the show goes on. We plan coverage around your venue, crowd size and schedule, and we report clearly after every event. Reach us today to book trained staff for your next gathering.</p>
    </div>
    <div class="specialize">
      <h2 class="specialize-title">WE SPECIALIZE!</h2>
      <p class="specialize-text">In providing professional, certified EMTs, Paramedics, Athletic Trainers, Nurses and Physicians for events, media productions, businesses, resorts, racing and sporting events across the Southwest. We have a lengthy and impressive list of clients and certified EMTs and Paramedics with extensive experience, ready on a moment's notice. We can tailor these services to meet nearly any need or budget.</p>
    </div>
    <div class="photo photo-ambulance" role="img" aria-label="Photo of an ambulance at an event"></div>
    <div class="photo photo-medic" role="img" aria-label="Photo of a medic in an orange shirt on duty"></div>
    <div class="photo photo-balloon" role="img" aria-label="Photo of a hot air balloon glowing at night"></div>
  </section>
  <div class="fold"></div>

</body>
</html>
```